Screen Tides - Report on digital habits and attitudes

We are a research company and we have written a PowerPoint Report to present the results of a series of surveys conducted in the last three years. The research is about the "Screen Tides": people are facing the opportunities and challanges of their lives transformed by the digital technologies. We have investigated a number of topics through thousands of interviews and we've analyzed the data presented in the PowerPoint document.
We're not quite satisfied with the look and feel of the report: it looks too flat and boring, too "basic" to be presented as a professional work, yet being just that. We'd like you to upgrade the graphics and style of the report up to the level of a professional research product. The document still needs to be fully editable (either text and charts) but you can rearrange all the contents as you please, adding images, changing font and text size, colors and whatever you think is necessary to reach our goal.

Target Market(s)

Media covering digital issues
Marketing executives
Public institutions and policy makers

Industry/Entity Type

Market Research

Requirements
Must have
• The treats of a professional work
Fully editable within PowerPoint (either text and charts)
Nice to have
• Smart images
Original organization of the pages
Colors and graphics coherent with the corvalmeadow.it logo/website look and feel
Should not have
• PPT document over 30 MBytes
Images violating copyright

```html
<!DOCTYPE html>
<html lang="it">
<head>
<meta charset="utf-8">
<title>Osservatorio Screen Tides – Report</title>
<link rel="stylesheet" href="https://fonts.googleapis.com/css2?family=Ubuntu:wght@300;400;500;700&display=swap">
<style>
:root{
  --orange:#f28c1e;
  --ink:#2b2b2b;
  --text:#4d4d4d;
  --muted:#8c8c8c;
  --rule:#dedede;
  --bar:#2f2f2f;
  --canvas:#ececec;
  --night:#141414;
  --white:#ffffff;
}
*{box-sizing:border-box}
html,body{margin:0;padding:0}
body{width:1200px;height:4640px;overflow:hidden;background:var(--canvas);font-family:'Ubuntu',sans-serif;color:var(--text)}
.book{display:grid;grid-template-columns:516px 516px;column-gap:50px;row-gap:39px;padding:40px 0 0 61px}
.page{width:516px;height:722px;position:relative;overflow:hidden;background:var(--white);box-shadow:0 2px 7px rgba(0,0,0,.18)}

/* brand */
.logo-tile{position:absolute;background:var(--white);display:flex;flex-direction:column;align-items:center;justify-content:center;gap:6px}
.logo-dot{border-radius:50%;background:var(--orange)}
.logo-name{font-family:'Ubuntu',sans-serif;font-weight:500;color:var(--ink);letter-spacing:1px;text-align:center;line-height:1.15}
.brandmark{position:absolute;top:34px;right:34px;display:flex;align-items:center;gap:5px}
.brandmark .logo-dot{width:11px;height:11px}
.brandmark .logo-name{font-size:6px}

/* covers */
.cover{color:var(--white)}
.cover-url{position:absolute;bottom:20px;left:0;right:0;text-align:center;font-size:7.5px;letter-spacing:6px;color:var(--orange)}
.accent{color:var(--orange)}
.cover-ring{background:linear-gradient(#2c2c2c,#171717)}
.cover-ring .logo-tile{top:28px;left:212px;width:92px;height:92px}
.cover-band{position:absolute;left:0;right:0;height:46px;background:#101010;display:flex;align-items:center;justify-content:center;font-size:27px;font-weight:500}
.cover-ring .cover-band{top:150px}
.ring-art{position:absolute;top:222px;left:38px;width:440px;height:440px;border-radius:50%;background:radial-gradient(circle,#6a4a2a 0%,#3a3a3a 35%,#262626 70%,#1d1d1d 100%);border:1px solid #444}

.cover-keys{background:#0c0c0c}
.key-grid{position:absolute;top:14px;left:250px;right:14px;bottom:46px;display:grid;grid-template-columns:1fr 1fr;grid-template-rows:1fr 1fr 1fr;gap:8px}
.key-grid div{background:linear-gradient(160deg,#4a4a4a,#161616)}
.cover-keys .acronym{position:absolute;top:62px;left:28px;font-size:64px;font-weight:700;line-height:1}
.cover-keys .stack{position:absolute;top:150px;left:28px;font-size:29px;font-weight:500;line-height:1.2}
.cover-keys .logo-tile{top:300px;left:30px;width:52px;height:52px;gap:3px}
.cover-keys .cover-url{left:28px;right:auto;text-align:left;font-size:6.5px;letter-spacing:4px}

.cover-city{background:var(--white)}
.city-top{position:absolute;top:0;left:0;right:0;height:498px;background:linear-gradient(#1a1a1a,#0a0a0a)}
.label-box{position:absolute;top:66px;left:34px;border:2px solid var(--white);padding:3px 8px;font-size:30px;font-weight:700;line-height:1}
.cover-city .stack{position:absolute;top:128px;left:34px;font-size:35px;font-weight:500;line-height:1.2}
.cover-city .logo-tile{top:66px;right:34px;width:78px;height:78px}
.city-art{position:absolute;top:372px;left:150px;width:300px;height:98px;background:linear-gradient(#f4f4f4,#cfcfcf);border-radius:4px 4px 0 0}
.city-orange{position:absolute;top:508px;left:0;right:0;bottom:0;background:var(--orange)}
.cover-city .cover-url{color:var(--white)}

.cover-globe{background:linear-gradient(#2a2a2a,#141414)}
.cover-globe .acronym{position:absolute;top:14px;left:20px;font-size:98px;font-weight:700;line-height:1}
.cover-globe .logo-tile{top:22px;right:26px;width:86px;height:86px}
.cover-globe .cover-band{top:150px;font-size:26px}
.globe-art{position:absolute;top:300px;left:93px;width:330px;height:330px;border-radius:50%;background:radial-gradient(circle at 45% 40%,#d9d9d9 0%,#8a8a8a 35%,#3a3a3a 70%,#1c1c1c 100%)}

/* index */
.index-strip{position:absolute;top:0;left:0;width:209px;height:100%;background:linear-gradient(#3b3b3b,#121212)}
.index-title{position:absolute;top:48px;left:22px;font-size:32px;font-weight:500;color:var(--white)}
.index-list{position:absolute;top:120px;left:194px;right:36px;margin:0;padding:0;list-style:none}
.index-list li{display:flex;align-items:center;height:61px}
.index-bullet{width:30px;height:30px;border-radius:50%;background:var(--orange);display:flex;align-items:center;justify-content:center;flex:none}
.index-label{flex:1;margin-left:26px;font-size:15px;color:var(--ink);border-bottom:1px solid var(--rule);padding:16px 0 14px;display:flex;justify-content:space-between}
.index-foot{position:absolute;bottom:16px;left:18px;width:170px;font-size:6px;color:var(--white);line-height:1.5}

/* content pages */
.sheet{padding:40px 36px 0}
.sheet-title{margin:0 0 18px;font-size:23px;font-weight:500;color:var(--ink)}
.sheet p{margin:0 0 6px;font-size:7.6px;line-height:1.6;text-align:justify;color:var(--text)}
.sheet strong{color:var(--ink);font-weight:700}
.cols{column-count:2;column-gap:18px}
.intro p{font-size:8.6px;line-height:1.75;margin-bottom:8px}
.grid2{display:grid;grid-template-columns:1fr 1fr;gap:18px}
.page-foot{position:absolute;bottom:14px;left:36px;right:36px;display:flex;justify-content:space-between;font-size:6px;color:var(--muted)}

.chart{border:1px solid var(--rule);margin:8px 0 10px;padding:0 0 6px}
.chart-title{font-size:7px;font-weight:700;color:var(--ink);text-align:center;padding:6px 0 4px;border-bottom:1px solid var(--rule);margin-bottom:6px}
.chart svg{display:block;width:100%}
.chart-note{font-size:5.5px;font-style:italic;color:var(--muted);text-align:center;margin-top:3px}

.bars{padding:0 14px}
.bar-row{display:grid;grid-template-columns:250px 1fr;gap:6px;align-items:center;height:13px}
.bar-label{font-size:5.8px;text-align:right;color:var(--text)}
.bar-track{display:flex;align-items:center;gap:4px}
.bar{height:9px;background:var(--bar)}
.bar-value{font-size:6px;font-weight:700;color:var(--orange)}

.dot-strip{margin:10px 0 12px}
.dot-strip-title{font-size:6px;color:var(--ink);margin-bottom:4px}

.profile{width:100%;border-collapse:collapse;margin:10px 0 14px;font-size:7px}
.profile caption{font-size:7.5px;font-weight:700;color:var(--ink);padding:6px;border:1px solid var(--rule);border-bottom:none}
.profile td{border-top:1px solid var(--rule);padding:6px 8px;vertical-align:top;color:var(--text)}
.profile td:first-child{width:40%;color:var(--ink)}
.profile{border:1px solid var(--rule)}
.bottom-row{display:grid;grid-template-columns:250px 1fr;gap:24px;align-items:center}
.couple-art{height:130px;background:linear-gradient(#9a9a9a,#4d4d4d)}
</style>
</head>
<body>
<main class="book">

  <!-- Cover: ring -->
  <section class="page cover cover-ring">
    <div class="logo-tile"><span class="logo-dot" style="width:26px;height:26px"></span><span class="logo-name" style="font-size:8px">CORVAL<br>MEADOW</span></div>
    <div class="cover-band"><span class="accent">Osservatorio</span>&nbsp;Screen Tides</div>
    <div class="ring-art" role="img" aria-label="Cerchi concentrici di icone digitali attorno a un simbolo centrale"></div>
    <div class="cover-url">WWW.CORVALMEADOW.IT</div>
  </section>

  <!-- Cover: keyboard -->
  <section class="page cover cover-keys">
    <div class="key-grid" role="img" aria-label="Riquadri fotografici di una tastiera scura"><div></div><div></div><div></div><div></div><div></div><div></div></div>
    <div class="acronym">OST</div>
    <div class="stack"><span class="accent">Osservatorio</span><br>Screen<br>Tides</div>
    <div class="logo-tile"><span class="logo-dot" style="width:14px;height:14px"></span><span class="logo-name" style="font-size:5px">CORVAL<br>MEADOW</span></div>
    <div class="cover-url">WWW.CORVALMEADOW.IT</div>
  </section>

  <!-- Cover: city -->
  <section class="page cover cover-city">
    <div class="city-top"></div>
    <div class="label-box">OST</div>
    <div class="stack"><span class="accent">Osservatorio</span><br>Screen<br>Tides</div>
    <div class="logo-tile"><span class="logo-dot" style="width:22px;height:22px"></span><span class="logo-name" style="font-size:7px">CORVAL<br>MEADOW</span></div>
    <div class="city-art" role="img" aria-label="Skyline bianco di una città con simboli di musica, denaro e grafici"></div>
    <div class="city-orange"></div>
    <div class="cover-url">WWW.CORVALMEADOW.IT</div>
  </section>

  <!-- Cover: globe -->
  <section class="page cover cover-globe">
    <div class="acronym">OST</div>
    <div class="logo-tile"><span class="logo-dot" style="width:24px;height:24px"></span><span class="logo-name" style="font-size:8px">CORVAL<br>MEADOW</span></div>
    <div class="cover-band"><span class="accent">Osservatorio</span>&nbsp;Screen Tides</div>
    <div class="globe-art" role="img" aria-label="Sfera di vetro con mappa del mondo e rete di connessioni luminose"></div>
    <div class="cover-url">WWW.CORVALMEADOW.IT</div>
  </section>

  <!-- Index -->
  <section class="page">
    <div class="index-strip" role="img" aria-label="Scrivania con computer in un ufficio in penombra"></div>
    <div class="index-title">Indice</div>
    <div class="brandmark"><span class="logo-dot"></span><span class="logo-name">CORVAL MEADOW</span></div>
    <ul class="index-list">
      <li><span class="index-bullet"><svg width="10" height="10" viewBox="0 0 10 10"><path d="M3 1l4 4-4 4" fill="none" stroke="#fff" stroke-width="1.6"/></svg></span><span class="index-label"><span>Introduction</span><span>01</span></span></li>
      <li><span class="index-bullet"><svg width="10" height="10" viewBox="0 0 10 10"><path d="M3 1l4 4-4 4" fill="none" stroke="#fff" stroke-width="1.6"/></svg></span><span class="index-label"><span>About Us</span><span>04</span></span></li>
      <li><span class="index-bullet"><svg width="10" height="10" viewBox="0 0 10 10"><path d="M3 1l4 4-4 4" fill="none" stroke="#fff" stroke-width="1.6"/></svg></span><span class="index-label"><span>Welcome Message</span><span>10</span></span></li>
      <li><span class="index-bullet"><svg width="10" height="10" viewBox="0 0 10 10"><path d="M3 1l4 4-4 4" fill="none" stroke="#fff" stroke-width="1.6"/></svg></span><span class="index-label"><span>Our Services</span><span>20</span></span></li>
      <li><span class="index-bullet"><svg width="10" height="10" viewBox="0 0 10 10"><path d="M3 1l4 4-4 4" fill="none" stroke="#fff" stroke-width="1.6"/></svg></span><span class="index-label"><span>Our Team</span><span>24</span></span></li>
      <li><span class="index-bullet"><svg width="10" height="10" viewBox="0 0 10 10"><path d="M3 1l4 4-4 4" fill="none" stroke="#fff" stroke-width="1.6"/></svg></span><span class="index-label"><span>Contact Us</span><span>28</span></span></li>
    </ul>
    <div class="index-foot">Screen Tides | dicembre 2021 |<br>© Corval Meadow 2021</div>
    <div class="page-foot" style="left:auto"><span>PAGE | 5</span></div>
  </section>

  <!-- Introduzione -->
  <section class="page sheet intro">
    <h2 class="sheet-title">Introduzione</h2>
    <div class="brandmark"><span class="logo-dot"></span><span class="logo-name">CORVAL MEADOW</span></div>
    <div class="cols">
      <p>Il digitale ha cambiato il mondo e un livello di profondità di cui non siamo ancora pienamente consapevoli. È facile riconoscere le manifestazioni del digitale nei <strong>comportamenti delle persone</strong> e notare come abbia trasformato abitudini e ritualità quotidiane.</p>
      <p>Non è altrettanto immediato comprendere quanto il digitale abbia modificato il <strong>mondo interiore</strong> e abbia inciso sul senso dell'identità, sulle emozioni, sui rapporti personali, sugli affetti e sul modo di concepire la società, i diritti e la libertà personale.</p>
      <p>L'obiettivo di questo lavoro di ricerca è raccontare la struttura e l'evoluzione di alcuni atteggiamenti di fondo che influenzano i comportamenti quotidiani legati alle tecnologie digitali. Le informazioni sono ricavate dalle dichiarazioni di campioni di individui chiamati a riflettere sull'<strong>ambiente connesso</strong> in cui vivono.</p>
      <p>L'analisi indaga le dinamiche cognitive e psicologiche che originano i comportamenti e descrive gli orientamenti di base sottostanti alle scelte, talvolta inconsapevoli, che danno forma alla dimensione digitale della vita.</p>
      <p>Vita non mediata dagli strumenti dell'ICT: persone introverse nella vita naturale possono avere una vita digitale ricca di relazioni e attività, così come persone di orientamento liberale possono assumere atteggiamenti reazionari nella dimensione digitale.</p>
      <p>La recente esperienza del lockdown per il Covid-19 ha <strong>accelerato l'evoluzione del fenomeno</strong> e ha esasperato alcuni aspetti della <strong>dimensione digitale della vita</strong>. Per alcuni mesi il mondo è stato un inedito e prezioso laboratorio di psicologia sociale.</p>
      <p>Per questi motivi Corval Meadow ha prodotto le analisi dei dati e ha anticipato l'uscita di questo rapporto, con l'obiettivo di seguire i fenomeni per un tempo più lungo, di almeno un decennio.</p>
      <p>Le innovazioni dell'epoca moderna hanno generato benessere diffuso: dalla medicina all'elettricità, dalla diffusione della conoscenza alla produzione di prodotti alimentari. La domanda che ci poniamo oggi è relativa alle tecnologie digitali: ci renderanno la vita più facile, la convivenza più pacifica, ci daranno una salute migliore?</p>
      <p><strong>In definitiva, il digitale ci renderà più felici?</strong></p>
    </div>
    <div class="page-foot"><span>Screen Tides | dicembre 2021 | © Corval Meadow 2021</span><span>PAGE | 6</span></div>
  </section>

  <!-- La ricerca -->
  <section class="page sheet">
    <h2 class="sheet-title">La ricerca</h2>
    <div class="brandmark"><span class="logo-dot"></span><span class="logo-name">CORVAL MEADOW</span></div>
    <div class="grid2">
      <div>
        <p>“L'ambiente connesso” è tutto ciò che accade perché siamo connessi alla rete: tutti i modi che, grazie alla connessione, permettono di comunicare con altre persone e tessere relazioni, informarsi, acquistare, pagare, lavorare e divertirsi.</p>
        <p>Alcune di queste attività fanno ormai parte della nostra vita quotidiana, altre probabilmente lo diventeranno nei prossimi anni. Ecco, tutto questo compone l'ambiente connesso.</p>
      </div>
      <div>
        <p>La popolazione online riesce quindi a rappresentare quella fetta di società italiana maggiormente impattata dal fenomeno della digitalizzazione e del mondo connesso, anche se con livelli di consapevolezza, stress, paure e atteggiamenti molto diversi.</p>
        <p>L'esigenza di capire il vissuto degli italiani su questi temi è nata in Corval Meadow nel 2018 e si è concretizzata con la prima rilevazione a gennaio 2019, una fotografia della situazione prima della pandemia.</p>
      </div>
    </div>
    <div class="dot-strip">
      <div class="dot-strip-title">Analisi di 27 aspetti dell'impatto del digitale nella vita quotidiana</div>
      <svg viewBox="0 0 444 26" width="444" height="26" aria-label="Ripartizione dei 27 aspetti analizzati">
        <g>
          <rect x="0" y="0" width="130" height="10" fill="#7bb661"/>
          <rect x="130" y="0" width="130" height="10" fill="#4f8fcf"/>
          <rect x="260" y="0" width="70" height="10" fill="#f28c1e"/>
          <rect x="330" y="0" width="114" height="10" fill="#d9534f"/>
        </g>
        <g font-size="5.5" font-family="Ubuntu, sans-serif" font-weight="700">
          <text x="65" y="21" text-anchor="middle" fill="#7bb661">8 domande sulle paure</text>
          <text x="195" y="21" text-anchor="middle" fill="#4f8fcf">8 domande sulle speranze</text>
          <text x="295" y="21" text-anchor="middle" fill="#f28c1e">4 di atteggiamento</text>
          <text x="387" y="21" text-anchor="middle" fill="#d9534f">7 sulla società digitale</text>
        </g>
      </svg>
    </div>
    <div class="grid2">
      <div><p>La ricerca si basa sull'analisi di 27 aspetti dell'impatto delle nuove tecnologie nella vita quotidiana, misurati con 19 ulteriori indicatori su comportamenti reali, atteggiamenti e giudizi. I temi sono stati rilevati su un campione rappresentativo degli oltre 40 milioni di italiani online.</p></div>
      <div><p>Intensificare le rilevazioni, che nel 2020 sono state tre: una pre-emergenza, una durante il primo lockdown e una durante il secondo. Nel documento sono mostrati i risultati relativi a cinque onde di ricerca che permettono di descrivere il mondo prima e dopo la pandemia.</p></div>
    </div>
    <div class="page-foot"><span>Screen Tides | dicembre 2021 | © Corval Meadow 2021</span><span>PAGE | 7</span></div>
  </section>

  <!-- Le paure 8 -->
  <section class="page sheet">
    <h2 class="sheet-title">Le paure</h2>
    <div class="brandmark"><span class="logo-dot"></span><span class="logo-name">CORVAL MEADOW</span></div>
    <p>Il digitale può fare paura per le conseguenze che produce sulla capacità cognitiva, nelle relazioni personali e sociali, fino a quelle internazionali. Molti non conoscono cosa ci sia dietro e da dove vengono certe scelte della tecnologia e ne percepiscono una minaccia. Inoltre, certi racconti sulle sorveglianze digitali alimentano un senso di sospetto diffuso.</p>
    <div class="chart">
      <div class="chart-title">Le paure e i sospetti</div>
      <div class="bars">
        <div class="bar-row"><span class="bar-label">Nell'ambiente connesso è più facile manipolare le persone</span><span class="bar-track"><span class="bar" style="width:80%"></span><span class="bar-value">80%</span></span></div>
        <div class="bar-row"><span class="bar-label">I ragazzi hanno rapporti più poveri a causa del digitale</span><span class="bar-track"><span class="bar" style="width:77%"></span><span class="bar-value">77%</span></span></div>
        <div class="bar-row"><span class="bar-label">Alcuni servizi sanno tutto di me e delle mie abitudini</span><span class="bar-track"><span class="bar" style="width:75%"></span><span class="bar-value">75%</span></span></div>
        <div class="bar-row"><span class="bar-label">I dispositivi riducono la nostra capacità di concentrazione</span><span class="bar-track"><span class="bar" style="width:71%"></span><span class="bar-value">71%</span></span></div>
        <div class="bar-row"><span class="bar-label">La rete porta a distinguere sempre meno tra vero e falso</span><span class="bar-track"><span class="bar" style="width:70%"></span><span class="bar-value">70%</span></span></div>
        <div class="bar-row"><span class="bar-label">Il digitale diminuisce la capacità di apprendimento</span><span class="bar-track"><span class="bar" style="width:42%"></span><span class="bar-value">42%</span></span></div>
        <div class="bar-row"><span class="bar-label">La democrazia corre rischi a causa del digitale</span><span class="bar-track"><span class="bar" style="width:35%"></span><span class="bar-value">35%</span></span></div>
        <div class="bar-row"><span class="bar-label">Preoccupazione per la salute fisica davanti agli schermi</span><span class="bar-track"><span class="bar" style="width:33%"></span><span class="bar-value">33%</span></span></div>
      </div>
      <div class="chart-note">Incidenza sul totale campione dei Top2Box di accordo</div>
    </div>
    <div class="grid2">
      <div><p>Il sospetto che il flusso di informazioni generato dalle tecnologie sia utilizzato con finalità di <strong>controllo o manipolazione</strong> è molto diffuso e riguarda otto individui su dieci. Il 77% si dichiara d'accordo con l'affermazione secondo la quale il digitale crea <strong>problemi di socialità</strong> nei ragazzi.</p></div>
      <div><p>Persone oltre i 54 anni di età. Così come tra i meno giovani trova conferma l'idea, più diffusa, che il digitale diminuisca le <strong>capacità di apprendimento</strong>. Le paure sulle conseguenze politiche e sociali del digitale sono più contenute e riguardano un terzo della popolazione.</p></div>
    </div>
    <div class="chart">
      <div class="chart-title">Il trend dell'indice di paura</div>
      <svg viewBox="0 0 440 92" aria-label="Andamento dell'indice di paura">
        <polyline points="40,56 130,50 220,24 310,40 400,40" fill="none" stroke="#555" stroke-width="1.4"/>
        <g fill="#2f2f2f"><circle cx="40" cy="56" r="2.5"/><circle cx="130" cy="50" r="2.5"/><circle cx="220" cy="24" r="2.5"/><circle cx="310" cy="40" r="2.5"/><circle cx="400" cy="40" r="2.5"/></g>
        <g font-size="7" font-family="Ubuntu, sans-serif" font-weight="700" fill="#2b2b2b" text-anchor="middle">
          <text x="40" y="70">58%</text><text x="130" y="64">59%</text><text x="220" y="16">62%</text><text x="310" y="32">60%</text><text x="400" y="32">60%</text>
        </g>
        <g font-size="6.5" font-family="Ubuntu, sans-serif" fill="#666" text-anchor="middle">
          <text x="40" y="88">feb 19</text><text x="130" y="88">ott 19</text><text x="220" y="88">feb 20</text><text x="310" y="88">mag 20</text><text x="400" y="88">nov 20</text>
        </g>
      </svg>
      <div class="chart-note">Incidenza sul totale campione dei Top2Box di accordo</div>
    </div>
    <div class="page-foot"><span>Screen Tides | dicembre 2021 | © Corval Meadow 2021</span><span>PAGE | 8</span></div>
  </section>

  <!-- Le paure 9 -->
  <section class="page sheet">
    <h2 class="sheet-title">Le paure</h2>
    <div class="brandmark"><span class="logo-dot"></span><span class="logo-name">CORVAL MEADOW</span></div>
    <div class="grid2">
      <div>
        <p>Otto persone su dieci ritengono che nell'ambiente digitale sia oggi più facile <strong>manipolare le persone</strong> rispetto al passato. Il riferimento al passato è relativo al Novecento, epoca in cui i mezzi di comunicazione di massa erano gestiti da pochi.</p>
        <div class="chart">
          <div class="chart-title">La manipolazione delle persone</div>
          <svg viewBox="0 0 220 80" aria-label="Andamento della manipolazione delle persone">
            <polyline points="18,28 62,36 106,44 150,28 194,20" fill="none" stroke="#555" stroke-width="1.2"/>
            <g font-size="6" font-family="Ubuntu, sans-serif" font-weight="700" fill="#2b2b2b" text-anchor="middle"><text x="18" y="22">79%</text><text x="62" y="30">78%</text><text x="106" y="55">77%</text><text x="150" y="22">79%</text><text x="194" y="14">80%</text></g>
            <g font-size="5.5" font-family="Ubuntu, sans-serif" fill="#666" text-anchor="middle"><text x="18" y="76">feb 19</text><text x="62" y="76">ott 19</text><text x="106" y="76">feb 20</text><text x="150" y="76">mag 20</text><text x="194" y="76">nov 20</text></g>
          </svg>
        </div>
        <p>Il sospetto sulla facilità di manipolazione delle persone è molto stabile e non si rileva alcuna tendenza significativa in tutto il periodo considerato.</p>
        <div class="chart">
          <div class="chart-title">Socialità e rapporti umani</div>
          <svg viewBox="0 0 220 80" aria-label="Andamento di socialità e rapporti umani">
            <polyline points="18,18 62,32 106,18 150,53 194,18" fill="none" stroke="#555" stroke-width="1.2"/>
            <g font-size="6" font-family="Ubuntu, sans-serif" font-weight="700" fill="#2b2b2b" text-anchor="middle"><text x="18" y="30">77%</text><text x="62" y="44">75%</text><text x="106" y="30">77%</text><text x="150" y="64">72%</text><text x="194" y="12">77%</text></g>
            <g font-size="5.5" font-family="Ubuntu, sans-serif" fill="#666" text-anchor="middle"><text x="18" y="76">feb 19</text><text x="62" y="76">ott 19</text><text x="106" y="76">feb 20</text><text x="150" y="76">mag 20</text><text x="194" y="76">nov 20</text></g>
          </svg>
        </div>
        <p>Il timore che il digitale ostacoli i rapporti e la socialità dei ragazzi è calato durante il primo lockdown, quando la tecnologia è apparsa come unico strumento di relazione.</p>
      </div>
      <div>
        <p>Diminuita la <strong>condanna</strong> verso le relazioni a distanza. La rilevazione successiva però ha mostrato che il cambiamento di giudizio è stato temporaneo e non si può ritenere un trend di lungo periodo.</p>
        <div class="chart">
          <div class="chart-title">Il Grande Fratello</div>
          <svg viewBox="0 0 220 80" aria-label="Andamento della percezione di sorveglianza">
            <polyline points="18,53 62,39 106,39 150,18 194,32" fill="none" stroke="#555" stroke-width="1.2"/>
            <g font-size="6" font-family="Ubuntu, sans-serif" font-weight="700" fill="#2b2b2b" text-anchor="middle"><text x="18" y="64">72%</text><text x="62" y="51">74%</text><text x="106" y="51">74%</text><text x="150" y="12">77%</text><text x="194" y="26">75%</text></g>
            <g font-size="5.5" font-family="Ubuntu, sans-serif" fill="#666" text-anchor="middle"><text x="18" y="76">feb 19</text><text x="62" y="76">ott 19</text><text x="106" y="76">feb 20</text><text x="150" y="76">mag 20</text><text x="194" y="76">nov 20</text></g>
          </svg>
        </div>
        <p>Tre rispondenti su quattro sono convinti che alcune <strong>organizzazioni sappiano tutto di noi</strong>, anche quando non siamo online. Il dato era leggermente aumentato nella primavera del 2020, probabilmente per le app di tracciamento dei contagi.</p>
        <p>Questo aspetto è stato incluso tra gli atteggiamenti di sospetto ma il giudizio negativo potrebbe riguardare solo una parte dei cittadini.</p>
      </div>
    </div>
    <div class="page-foot"><span>Screen Tides | dicembre 2021 | © Corval Meadow 2021</span><span>PAGE | 9</span></div>
  </section>

  <!-- Le speranze 10 -->
  <section class="page sheet">
    <h2 class="sheet-title">Le speranze</h2>
    <div class="brandmark"><span class="logo-dot"></span><span class="logo-name">CORVAL MEADOW</span></div>
    <p>Un italiano su due guarda alla diffusione del digitale con un atteggiamento positivo, fiducioso nel fatto che il progresso possa avere un impatto virtuoso su diversi ambiti della vita quotidiana. La speranza più diffusa è la semplificazione conseguente all'accesso alle informazioni e ai servizi.</p>
    <div class="chart">
      <div class="chart-title">Le speranze e le attese</div>
      <div class="bars">
        <div class="bar-row"><span class="bar-label">Il digitale semplifica la nostra vita di cittadini</span><span class="bar-track"><span class="bar" style="width:76%"></span><span class="bar-value">76%</span></span></div>
        <div class="bar-row"><span class="bar-label">C'è una generale crescita di competenze grazie al digitale</span><span class="bar-track"><span class="bar" style="width:72%"></span><span class="bar-value">72%</span></span></div>
        <div class="bar-row"><span class="bar-label">Le Smart Home con il digitale renderanno la vita migliore</span><span class="bar-track"><span class="bar" style="width:54%"></span><span class="bar-value">54%</span></span></div>
        <div class="bar-row"><span class="bar-label">Le Smart City renderanno la qualità della vita più elevata</span><span class="bar-track"><span class="bar" style="width:53%"></span><span class="bar-value">53%</span></span></div>
        <div class="bar-row"><span class="bar-label">Il digitale porterà più trasparenza nell'informazione</span><span class="bar-track"><span class="bar" style="width:53%"></span><span class="bar-value">53%</span></span></div>
        <div class="bar-row"><span class="bar-label">La partecipazione dei cittadini migliora grazie al digitale</span><span class="bar-track"><span class="bar" style="width:42%"></span><span class="bar-value">42%</span></span></div>
        <div class="bar-row"><span class="bar-label">Il lavoro a distanza diventerà più diffuso e più produttivo</span><span class="bar-track"><span class="bar" style="width:42%"></span><span class="bar-value">42%</span></span></div>
        <div class="bar-row"><span class="bar-label">Il digitale migliorerà la vita democratica del paese</span><span class="bar-track"><span class="bar" style="width:17%"></span><span class="bar-value">17%</span></span></div>
      </div>
      <div class="chart-note">Incidenza sul totale campione dei Top2Box di accordo</div>
    </div>
    <div class="grid2">
      <div><p>La maggioranza dei cittadini ripone una grande fiducia nelle smart technologies che ci si aspetta siano in grado di rendere gli ambienti in cui viviamo più vivibili. Il tema dell'informazione online, invece, divide la popolazione tra chi ritiene che sia più trasparente.</p></div>
      <div><p>Impatto positivo sul sistema informativo e chi non vede un miglioramento della qualità. Pochi si aspettano effetti positivi delle tecnologie digitali in ambito sanitario, sul funzionamento del sistema democratico e sull'emersione del merito.</p></div>
    </div>
    <div class="chart">
      <div class="chart-title">Il trend dell'indice di speranza</div>
      <svg viewBox="0 0 440 92" aria-label="Andamento dell'indice di speranza">
        <polyline points="40,42 130,60 220,33 310,24 400,33" fill="none" stroke="#555" stroke-width="1.4"/>
        <g fill="#2f2f2f"><circle cx="40" cy="42" r="2.5"/><circle cx="130" cy="60" r="2.5"/><circle cx="220" cy="33" r="2.5"/><circle cx="310" cy="24" r="2.5"/><circle cx="400" cy="33" r="2.5"/></g>
        <g font-size="7" font-family="Ubuntu, sans-serif" font-weight="700" fill="#2b2b2b" text-anchor="middle">
          <text x="40" y="56">53%</text><text x="130" y="74">51%</text><text x="220" y="25">54%</text><text x="310" y="16">55%</text><text x="400" y="47">54%</text>
        </g>
        <g font-size="6.5" font-family="Ubuntu, sans-serif" fill="#666" text-anchor="middle">
          <text x="40" y="88">feb 19</text><text x="130" y="88">ott 19</text><text x="220" y="88">feb 20</text><text x="310" y="88">mag 20</text><text x="400" y="88">nov 20</text>
        </g>
      </svg>
      <div class="chart-note">Incidenza sul totale campione dei Top2Box di accordo</div>
    </div>
    <div class="page-foot"><span>Screen Tides | dicembre 2021 | © Corval Meadow 2021</span><span>PAGE | 10</span></div>
  </section>

  <!-- Le speranze 11 -->
  <section class="page sheet">
    <h2 class="sheet-title">Le speranze</h2>
    <div class="brandmark"><span class="logo-dot"></span><span class="logo-name">CORVAL MEADOW</span></div>
    <div class="grid2">
      <div>
        <p><strong>«Il digitale semplificherà la nostra vita di cittadini»</strong>: ne sono convinti circa tre italiani su quattro. L'adesione a questa affermazione è diminuita in modo significativo durante l'emergenza, per poi tornare a rafforzarsi quando la tecnologia ha mostrato di essere uno strumento abilitante.</p>
        <div class="chart">
          <div class="chart-title">Il digitale semplifica la vita</div>
          <svg viewBox="0 0 220 80" aria-label="Andamento della semplificazione della vita">
            <polyline points="18,28 62,40 106,58 150,28 194,22" fill="none" stroke="#f28c1e" stroke-width="1.2"/>
            <g fill="#f28c1e"><circle cx="18" cy="28" r="9"/><circle cx="62" cy="40" r="9"/><circle cx="106" cy="58" r="9"/><circle cx="150" cy="28" r="9"/><circle cx="194" cy="22" r="9"/></g>
            <g font-size="5.5" font-family="Ubuntu, sans-serif" font-weight="700" fill="#fff" text-anchor="middle"><text x="18" y="30">77%</text><text x="62" y="42">75%</text><text x="106" y="60">72%</text><text x="150" y="30">77%</text><text x="194" y="24">78%</text></g>
            <g font-size="5.5" font-family="Ubuntu, sans-serif" fill="#666" text-anchor="middle"><text x="18" y="77">feb 19</text><text x="62" y="77">ott 19</text><text x="106" y="77">feb 20</text><text x="150" y="77">mag 20</text><text x="194" y="77">nov 20</text></g>
          </svg>
        </div>
        <p>I benefici della diffusione del digitale sulla qualità della vita all'interno delle case e nelle città sono evidenti a circa un italiano su due. L'entusiasmo per la <strong>democrazia partecipativa</strong> e per <strong>l'informazione diffusa</strong>, con i conseguenti benefici sul funzionamento del sistema democratico, non decolla e anzi si sta spegnendo col tempo.</p>
      </div>
      <div>
        <p>In costante crescita invece la convinzione che la diffusione online dell'informazione ne aumenti la qualità e renda il sistema nel suo complesso <strong>più trasparente</strong>.</p>
        <div class="chart">
          <div class="chart-title">Informazione più trasparente</div>
          <svg viewBox="0 0 220 80" aria-label="Andamento della trasparenza dell'informazione">
            <polyline points="18,50 62,44 106,38 150,26 194,20" fill="none" stroke="#999" stroke-width="1.2"/>
            <g fill="#a6a6a6"><circle cx="18" cy="50" r="9"/><circle cx="62" cy="44" r="9"/><circle cx="106" cy="38" r="9"/><circle cx="150" cy="26" r="9"/><circle cx="194" cy="20" r="9"/></g>
            <g font-size="5.5" font-family="Ubuntu, sans-serif" font-weight="700" fill="#fff" text-anchor="middle"><text x="18" y="52">48%</text><text x="62" y="46">49%</text><text x="106" y="40">50%</text><text x="150" y="28">52%</text><text x="194" y="22">53%</text></g>
            <g font-size="5.5" font-family="Ubuntu, sans-serif" fill="#666" text-anchor="middle"><text x="18" y="77">feb 19</text><text x="62" y="77">ott 19</text><text x="106" y="77">feb 20</text><text x="150" y="77">mag 20</text><text x="194" y="77">nov 20</text></g>
          </svg>
        </div>
        <p>Una convinzione largamente diffusa è che stiamo vivendo una generale crescita di competenze trainata dal digitale e il Covid-19 ha certamente accelerato questo fenomeno: lo smart working, la didattica a distanza e gli acquisti online hanno contribuito ad aumentare le competenze digitali.</p>
        <div class="chart">
          <div class="chart-title">Generale crescita di competenze</div>
          <svg viewBox="0 0 220 80" aria-label="Andamento della crescita di competenze">
            <polyline points="18,38 62,56 106,38 150,26 194,20" fill="none" stroke="#999" stroke-width="1.2"/>
            <g fill="#a6a6a6"><circle cx="18" cy="38" r="9"/><circle cx="62" cy="56" r="9"/><circle cx="106" cy="38" r="9"/><circle cx="150" cy="26" r="9"/><circle cx="194" cy="20" r="9"/></g>
            <g font-size="5.5" font-family="Ubuntu, sans-serif" font-weight="700" fill="#fff" text-anchor="middle"><text x="18" y="40">69%</text><text x="62" y="58">66%</text><text x="106" y="40">69%</text><text x="150" y="28">71%</text><text x="194" y="22">72%</text></g>
            <g font-size="5.5" font-family="Ubuntu, sans-serif" fill="#666" text-anchor="middle"><text x="18" y="77">feb 19</text><text x="62" y="77">ott 19</text><text x="106" y="77">feb 20</text><text x="150" y="77">mag 20</text><text x="194" y="77">nov 20</text></g>
          </svg>
        </div>
      </div>
    </div>
    <div class="page-foot"><span>Screen Tides | dicembre 2021 | © Corval Meadow 2021</span><span>PAGE | 11</span></div>
  </section>

  <!-- Le paure 12 -->
  <section class="page sheet">
    <h2 class="sheet-title">Le paure</h2>
    <div class="brandmark"><span class="logo-dot"></span><span class="logo-name">CORVAL MEADOW</span></div>
    <p>All'interno di questo gruppo di persone prevalgono sentimenti negativi: la paura di non avere totalmente il controllo delle attività che si svolgono online, il timore sui temi della privacy e il sospetto che le informazioni personali possano essere manipolate con una conseguente limitazione della libertà personale.</p>
    <p>Per non negare la funzione democratica della rete nell'accesso universale all'informazione e la conseguente maggiore trasparenza, questo gruppo si rifugia in un comportamento prudente e misurato. Nonostante queste chiusure, il bilancio delle novità è negativo e il digitale è vissuto come un problema da gestire con strumenti adeguati.</p>
    <table class="profile">
      <caption>Caratteristiche principali</caption>
      <tr><td>Dimensione</td><td>17% del campione, 6,7 milioni di persone</td></tr>
      <tr><td>Caratteristiche sociodemo</td><td>Mezza età (35-54 anni), grandi centri del Nord, elevata concentrazione di laureati</td></tr>
      <tr><td>Relazione col digitale e la tecnologia</td><td>Lavorano al PC, acquistano abitualmente online e usano app e servizi per la casa</td></tr>
      <tr><td>Parole chiave</td><td>#privacy #controllo #diffidenza #sorveglianza</td></tr>
      <tr><td>Emozioni vissute online</td><td>Positive e negative in egual misura</td></tr>
    </table>
    <div class="bottom-row">
      <div class="chart">
        <svg viewBox="0 0 250 92" aria-label="Andamento della quota del gruppo">
          <polygon points="0,44 84,44 84,38 96,50 84,62 84,56 0,56" fill="#f28c1e"/>
          <polyline points="20,50 70,68 125,20 175,26 225,68" fill="none" stroke="#555" stroke-width="1.2"/>
          <g font-size="6.5" font-family="Ubuntu, sans-serif" font-weight="700" fill="#2b2b2b" text-anchor="middle"><text x="20" y="40">51%</text><text x="70" y="62">48%</text><text x="125" y="14">56%</text><text x="175" y="18">55%</text><text x="225" y="62">48%</text></g>
          <g font-size="6" font-family="Ubuntu, sans-serif" fill="#666" text-anchor="middle"><text x="20" y="88">feb 19</text><text x="70" y="88">ott 19</text><text x="125" y="88">feb 20</text><text x="175" y="88">mag 20</text><text x="225" y="88">nov 20</text></g>
        </svg>
      </div>
      <div class="couple-art" role="img" aria-label="Ritratto di una coppia in posa davanti a una casa di campagna"></div>
    </div>
    <div class="page-foot"><span>Screen Tides | dicembre 2021 | © Corval Meadow 2021</span><span>PAGE | 12</span></div>
  </section>

</main>
</body>
</html>
```